Business Cards for a Dating Coach/Social Dynamics company
Velvet Compass
Professional
Ted
Dating Instructor
4872 Marlow Terrace, #9
Miami Beach, FL 33139
Skyheron@velvetcompasslife.com
www.velvetcompasslife.com

```html
<!DOCTYPE html>
<html lang="en">
<head>
<meta charset="UTF-8">
<title>Velvet Compass — Business Card</title>
<link href="https://fonts.googleapis.com/css2?family=Open+Sans:wght@400;600&display=swap" rel="stylesheet">
<style>
  :root {
    --page-bg: #ece9e4;
    --card-bg: #58595b;
    --text-light: #f2f2f2;
    --accent-red: #d9382c;
  }
  html, body {
    margin: 0;
    padding: 0;
    width: 1200px;
    height: 914px;
    overflow: hidden;
    background: var(--page-bg);
    font-family: "Open Sans", sans-serif;
  }
  .canvas {
    width: 1200px;
    height: 914px;
    display: flex;
    align-items: center;
    justify-content: center;
  }
  .business-card {
    position: relative;
    width: 900px;
    height: 514px;
    background: var(--card-bg);
    color: var(--text-light);
    box-shadow: 0 10px 30px rgba(0,0,0,0.18);
  }
  .brand {
    position: absolute;
    top: 120px;
    left: 0;
    right: 0;
    display: flex;
    flex-direction: column;
    align-items: center;
  }
  .brand-row {
    display: flex;
    align-items: center;
    gap: 16px;
  }
  .brand-dot {
    width: 46px;
    height: 46px;
    border-radius: 50%;
    background: var(--accent-red);
  }
  .brand-name {
    font-size: 44px;
    font-weight: 400;
    color: var(--text-light);
    letter-spacing: 0.5px;
  }
  .brand-tagline {
    margin-top: 6px;
    margin-left: 62px;
    font-size: 13px;
    letter-spacing: 2.5px;
    text-transform: uppercase;
    color: var(--text-light);
  }
  .person {
    position: absolute;
    top: 285px;
    left: 0;
    right: 0;
    text-align: center;
    font-size: 22px;
  }
  .person-name { color: var(--accent-red); font-weight: 600; }
  .person-divider { color: var(--accent-red); margin: 0 8px; }
  .person-role { color: var(--text-light); }
  .contact {
    position: absolute;
    top: 360px;
    left: 150px;
    right: 120px;
    font-size: 15px;
    line-height: 30px;
  }
  .contact-row { display: flex; gap: 26px; }
  .contact-item { display: flex; align-items: center; gap: 9px; }
  .contact-icon { width: 14px; height: 14px; flex: none; }
</style>
</head>
<body>
<div class="canvas">
  <section class="business-card">
    <div class="brand">
      <div class="brand-row">
        <span class="brand-dot"></span>
        <span class="brand-name">Velvet Compass</span>
      </div>
      <div class="brand-tagline">Lifestyle and Dating Specialists</div>
    </div>

    <div class="person">
      <span class="person-name">Ted</span><span class="person-divider">|</span><span class="person-role">Dating Instructor</span>
    </div>

    <div class="contact">
      <div class="contact-row">
        <span class="contact-item">
          <svg class="contact-icon" viewBox="0 0 14 14"><circle cx="7" cy="7" r="7" fill="var(--accent-red)"/><path d="M7 3.2a2.4 2.4 0 0 0-2.4 2.4C4.6 7.6 7 10.6 7 10.6s2.4-3 2.4-5A2.4 2.4 0 0 0 7 3.2z" fill="#fff"/></svg>
          4872 Marlow Terrace, #9 Miami Beach, FL 33139
        </span>
        <span class="contact-item">
          <svg class="contact-icon" viewBox="0 0 14 14"><circle cx="7" cy="7" r="7" fill="var(--accent-red)"/><path d="M4.6 3.8l1.4-.3.8 1.8-.9.7a5 5 0 0 0 2.1 2.1l.7-.9 1.8.8-.3 1.4c-3 .3-5.9-2.6-5.6-5.6z" fill="#fff"/></svg>
          305-555-0182
        </span>
      </div>
      <div class="contact-row">
        <span class="contact-item">
          <svg class="contact-icon" viewBox="0 0 14 14"><circle cx="7" cy="7" r="7" fill="var(--accent-red)"/><rect x="3.6" y="4.6" width="6.8" height="4.8" fill="none" stroke="#fff" stroke-width="0.9"/><path d="M3.6 4.6L7 7.4l3.4-2.8" fill="none" stroke="#fff" stroke-width="0.9"/></svg>
          Skyheron@velvetcompasslife.com
        </span>
        <span class="contact-item">
          <svg class="contact-icon" viewBox="0 0 14 14"><circle cx="7" cy="7" r="7" fill="var(--accent-red)"/><circle cx="7" cy="7" r="3.4" fill="none" stroke="#fff" stroke-width="0.9"/><path d="M3.6 7h6.8M7 3.6c-1.6 1.8-1.6 5 0 6.8M7 3.6c1.6 1.8 1.6 5 0 6.8" fill="none" stroke="#fff" stroke-width="0.8"/></svg>
          www.velvetcompasslife.com
        </span>
      </div>
    </div>
  </section>
</div>
</body>
</html>
```